Tidal Quill is a premium Spa and Salon only professional tanning brand.

We need a email template/newsletter that we can send to our client base any time we would like to share information with them.
Whether this is launching our Christmas gift, or sharing up and coming training dates it will be another avenue for us to stay in touch with our clients.
We like to think ourselves as the 'Verrington handbag' in the tanning world, Tidal Quill is a brand that is desirable and exclusive and has people hooked once they trial the brand and are blown away by the results.
www.tidal-quill-example.com

```html
<!DOCTYPE html>
<html lang="en">
<head>
<meta charset="utf-8">
<title>Tidal Quill — Newsletter</title>
<link rel="stylesheet" href="https://fonts.googleapis.com/css2?family=Questrial&family=Montserrat:wght@500;700&family=Arimo:wght@400;700&display=swap">
<style>
  :root {
    --ink: #1a1a1a;
    --white: #ffffff;
    --grey-text: #8a8a8a;
    --grey-line: #cfcfcf;
    --social-band: #ebebeb;
    --footer: #000000;
    --stockist: #c88a5f;
    --link: #1fa3e6;
    --accent-blue: #1fa0e0;
    --accent-yellow: #f3df00;
    --accent-cyan: #00d6e6;
    --accent-pink: #e6006d;
    --overlay: rgba(25, 20, 16, 0.62);
    --display: "Questrial", "Century Gothic", sans-serif;
    --strong: "Montserrat", "Century Gothic", sans-serif;
    --body: "Arimo", Arial, sans-serif;
  }
  * { box-sizing: border-box; margin: 0; padding: 0; }
  html, body { width: 1200px; height: 3854px; overflow: hidden; background: var(--white); }
  .page { position: relative; width: 1200px; height: 3854px; overflow: hidden; font-family: var(--body); color: var(--ink); }

  /* Hero */
  .hero { position: absolute; left: 0; top: 0; width: 1200px; height: 1300px; }
  .hero-photo { position: absolute; inset: 0;
    background: radial-gradient(ellipse at 35% 30%, #b08a62 0%, #6b4c35 30%, #3a2a20 60%, #221a15 100%); }
  .brand-mark { position: absolute; right: 44px; top: 26px; text-align: right;
    font-family: var(--display); font-size: 104px; line-height: 86px; color: var(--white); letter-spacing: 2px; text-transform: uppercase; }
  .tagline { position: absolute; left: 745px; top: 855px; width: 455px; height: 148px;
    background: rgba(20, 14, 10, 0.72); padding: 18px 0 0 17px; }
  .tagline-lead { font-family: var(--display); font-size: 50px; line-height: 56px; color: var(--accent-yellow); text-transform: uppercase; }
  .tagline-main { font-family: var(--strong); font-weight: 700; font-size: 52px; line-height: 60px; color: var(--white); text-transform: uppercase; letter-spacing: 1px; }

  .hero-edge { position: absolute; left: 0; top: 1000px; }

  /* Product cards */
  .product { position: absolute; width: 555px; overflow: hidden; }
  .product-photo { position: absolute; inset: 0; }
  .product--gradual { left: 31px; top: 1119px; height: 675px; clip-path: polygon(0 0, 100% 105px, 100% 100%, 0 570px); }
  .product--gradual .product-photo { background: linear-gradient(135deg, #8a7866 0%, #b28a55 45%, #d2a236 75%, #6e5438 100%); }
  .product--mist { left: 617px; top: 1230px; height: 676px; clip-path: polygon(0 0, 100% 106px, 100% 100%, 0 570px); }
  .product--mist .product-photo { background: linear-gradient(150deg, #d9a018 0%, #d8552a 40%, #9c2a2a 65%, #7e9a2c 100%); }
  .product--dark { left: 31px; top: 1787px; height: 703px; clip-path: polygon(0 0, 100% 105px, 100% 100%, 0 100%); }
  .product--dark .product-photo { background: linear-gradient(135deg, #d8d2cb 0%, #b59a86 45%, #6e4f3f 80%, #cfc8c0 100%); }
  .product--bronze { left: 617px; top: 1898px; height: 592px; clip-path: polygon(0 0, 100% 106px, 100% 100%, 0 100%); }
  .product--bronze .product-photo { background: linear-gradient(140deg, #9a9a9a 0%, #5d5d5d 40%, #1e1e1e 65%, #8c8c8c 100%); }

  .product-info { position: absolute; left: 0; width: 555px; background: var(--overlay); padding: 20px 31px 0; color: var(--white); }
  .product--gradual .product-info { top: 261px; height: 300px; }
  .product--mist .product-info { top: 253px; height: 423px; }
  .product--dark .product-info { top: 390px; height: 313px; }
  .product--bronze .product-info { top: 279px; height: 313px; }

  .product-name { font-family: var(--display); font-weight: 400; font-size: 54px; line-height: 60px; }
  .product-variant { font-family: var(--display); font-size: 26px; line-height: 34px; margin-bottom: 16px; }
  .product-copy { font-family: var(--body); font-size: 18.5px; line-height: 27px; margin-bottom: 20px; }
  .product-button { display: inline-block; padding: 12px 18px; font-family: var(--strong); font-weight: 700; font-size: 16px; color: var(--ink); text-decoration: none; text-transform: uppercase; }

  .product--gradual .product-name { color: var(--accent-blue); }
  .product--gradual .product-button { background: var(--accent-blue); }
  .product--mist .product-name { color: var(--accent-yellow); }
  .product--mist .product-button { background: var(--accent-yellow); }
  .product--dark .product-name { color: var(--accent-cyan); }
  .product--dark .product-button { background: var(--accent-cyan); }
  .product--bronze .product-name { color: var(--accent-pink); }
  .product--bronze .product-button { background: var(--accent-pink); }

  /* Newsletter */
  .newsletter { position: absolute; left: 72px; top: 2560px; width: 1056px; }
  .newsletter-title { font-family: var(--display); font-size: 52px; line-height: 62px; text-transform: uppercase; font-weight: 400; }
  .newsletter-title strong { font-family: var(--strong); font-weight: 700; letter-spacing: 1px; }
  .signup { position: absolute; left: 463px; top: 20px; display: flex; height: 78px; }
  .signup-field { width: 437px; border: 2px solid var(--ink); font-family: var(--body); font-size: 24px; padding: 0 26px; display: flex; align-items: center; }
  .signup-button { width: 154px; background: var(--ink); color: var(--white); font-family: var(--strong); font-weight: 700; font-size: 22px; display: flex; align-items: center; justify-content: center; text-transform: uppercase; }
  .newsletter-note { margin-top: 34px; font-size: 19.5px; line-height: 33px; color: var(--grey-text); }
  .unsubscribe { display: inline-block; margin-top: 26px; font-size: 20px; color: var(--link); text-decoration: underline; }

  /* Stockist */
  .stockist { position: absolute; left: 0; top: 2917px; width: 1200px; height: 334px; background: var(--stockist); text-align: center; }
  .stockist-title { font-family: var(--display); font-weight: 400; font-size: 56px; color: var(--white); margin-top: 48px; line-height: 64px; }
  .stockist-rule { width: 128px; height: 5px; background: var(--white); margin: 20px auto 0; }
  .stockist-field { position: absolute; top: 198px; width: 475px; height: 75px; background: var(--white); display: flex; align-items: center; justify-content: space-between; padding: 0 24px; font-size: 22px; color: #a5a5a5; }
  .stockist-field--country { left: 108px; }
  .stockist-field--search { left: 617px; }

  /* Contact */
  .details { position: absolute; left: 0; top: 3251px; width: 1200px; height: 283px; }
  .details-col { position: absolute; top: 52px; }
  .details-col--address { right: 642px; text-align: right; }
  .details-col--contact { left: 648px; }
  .details-heading { font-family: var(--display); font-weight: 400; font-size: 40px; line-height: 48px; color: var(--ink); margin-bottom: 20px; }
  .details-line { font-size: 19px; line-height: 33.5px; color: var(--grey-text); }
  .details-line a { color: var(--link); text-decoration: none; }

  .social { position: absolute; left: 0; top: 3534px; width: 1200px; height: 124px; background: var(--social-band); }

  .footer { position: absolute; left: 0; top: 3658px; width: 1200px; height: 196px; background: var(--footer); text-align: center; padding-top: 44px;
    font-family: var(--display); font-size: 60px; line-height: 56px; color: var(--white); text-transform: uppercase; letter-spacing: 2px; }
</style>
</head>
<body>
<div class="page">

  <header class="hero">
    <div class="hero-photo" role="img" aria-label="Portrait photograph of a blonde model in a brown leather jacket"></div>
    <div class="brand-mark">Tidal<br>Quill</div>
    <div class="tagline">
      <div class="tagline-lead">A revolution in</div>
      <div class="tagline-main">Self tanning</div>
    </div>
  </header>

  <svg class="hero-edge" width="1200" height="400" viewBox="0 1000 1200 400" aria-hidden="true">
    <polygon points="0,1054 1200,1272 1200,1400 0,1400" fill="#ffffff"/>
    <line x1="0" y1="1072" x2="1200" y2="1290" stroke="#cfcfcf" stroke-width="2"/>
    <line x1="0" y1="1086" x2="1200" y2="1304" stroke="#cfcfcf" stroke-width="2"/>
  </svg>

  <article class="product product--gradual">
    <div class="product-photo" role="img" aria-label="Photograph of a model with wavy blonde hair in a mustard coat"></div>
    <div class="product-info">
      <h2 class="product-name">Gradual Tan</h2>
      <p class="product-variant">Daily Lotion</p>
      <p class="product-copy">Much like our Gradual Tan, our Original and Dark formulas contain an organic formula that comes enriched with the same deep moisturisers.</p>
      <a class="product-button" href="#">View product</a>
    </div>
  </article>

  <article class="product product--mist">
    <div class="product-photo" role="img" aria-label="Photograph of a smiling model in a red beret and colourful scarf"></div>
    <div class="product-info">
      <h2 class="product-name">Tanning Mist</h2>
      <p class="product-variant">Orginal</p>
      <p class="product-copy">This organic formula is enriched with deep moisturisers and exotic botanical extracts that tone and firm the skin fighting cellulite whilst developing a naturally youthful, sunkissed glow.</p>
      <a class="product-button" href="#">View product</a>
    </div>
  </article>

  <article class="product product--dark">
    <div class="product-photo" role="img" aria-label="Photograph of a brunette model in a white top"></div>
    <div class="product-info">
      <h2 class="product-name">Tanning Mist</h2>
      <p class="product-variant">Dark</p>
      <p class="product-copy">For those with darker skin tones or this preference, these additional products provide the option of a richer darker colour.</p>
      <a class="product-button" href="#">View product</a>
    </div>
  </article>

  <article class="product product--bronze">
    <div class="product-photo" role="img" aria-label="Photograph of a model in a black beanie and sunglasses"></div>
    <div class="product-info">
      <h2 class="product-name">New Bronze Mist</h2>
      <p class="product-variant">Orginal</p>
      <p class="product-copy">This organic formula is enriched with deep moisturisers and exotic botanical extracts that tone and firm the skin.</p>
      <a class="product-button" href="#">View product</a>
    </div>
  </article>

  <section class="newsletter">
    <h2 class="newsletter-title">Sign up for our<br><strong>Newsletter</strong></h2>
    <div class="signup">
      <div class="signup-field">Enter your Email</div>
      <div class="signup-button">Sign up!</div>
    </div>
    <p class="newsletter-note">Contrary to popular belief, Lorem Ipsum is not simply random text. It has roots in a piece of classical Latin literature from 45 BC, making it over 2000 years old.</p>
    <a class="unsubscribe" href="#">Unsubscribe</a>
  </section>

  <section class="stockist">
    <h2 class="stockist-title">Find a stockist</h2>
    <div class="stockist-rule"></div>
    <div class="stockist-field stockist-field--country">
      <span>Select Country</span>
      <svg width="22" height="14" viewBox="0 0 22 14" aria-hidden="true"><polyline points="2,2 11,11 20,2" fill="none" stroke="#8a8a8a" stroke-width="3"/></svg>
    </div>
    <div class="stockist-field stockist-field--search">
      <span>Search...</span>
      <svg width="22" height="22" viewBox="0 0 22 22" aria-hidden="true"><circle cx="9" cy="9" r="6.5" fill="none" stroke="#8a8a8a" stroke-width="3"/><line x1="14" y1="14" x2="20" y2="20" stroke="#8a8a8a" stroke-width="3"/></svg>
    </div>
  </section>

  <section class="details">
    <div class="details-col details-col--address">
      <h3 class="details-heading">Address</h3>
      <p class="details-line">Millhaven Enterprise Centre</p>
      <p class="details-line">Larkfield Road Industrial Estate</p>
      <p class="details-line">Millhaven, County Down BT00 1QX</p>
    </div>
    <div class="details-col details-col--contact">
      <h3 class="details-heading">Contact</h3>
      <p class="details-line">+00 (12) 345 678</p>
      <p class="details-line">+00 (12) 345 679</p>
      <p class="details-line"><a href="#">hello@tidal-quill-example.com</a></p>
    </div>
  </section>

  <nav class="social" aria-label="Social links">
    <svg width="1200" height="124" viewBox="0 0 1200 124" aria-hidden="true">
      <g fill="#9a9a9a">
        <circle cx="463" cy="64" r="14"/>
        <circle cx="527" cy="64" r="14"/>
        <circle cx="599" cy="64" r="14"/>
        <circle cx="668" cy="64" r="14"/>
        <circle cx="738" cy="64" r="14"/>
      </g>
    </svg>
  </nav>

  <footer class="footer">Tidal<br>Quill</footer>

</div>
</body>
</html>
```